Pelton|Marsh & Quillan business card contest

We need a logo for an upscale boutique diversified company involved in real estate, investments, cattle, and more. Our businesses DO NOT need to be reflected in the business card nor do we want them noted. This is our logo and colors and we love our logo and colors. Our logo looks best against a black background and we like to include the firm name in our logo usage. importantly, the names Pelton and Marsh are separated by | not / and we use an ampersand not the word and.
On the front of the card, we want to include:
company logo and name (Pelton|Marsh & Quillan)
on the back, we would definitely include:
address, email, cell #
logo and name (smaller size than front)

The variable will be location of individual name and title (mine for example is ) - whether on the front OR on the back. interested in variations from which to choose
Dr. Neil R. Whitcombe, CFA
Scientifique des Fusées Financières

we would like to use contemporary symbols for address, email address, cell # with an option for web site that we do not intend to use initially. we like two sided cards and believe this design should use four rounded corners with the standard size. we prefer thicker card stock and may look at metal.

```html
<!DOCTYPE html>
<html lang="en">
<head>
<meta charset="utf-8">
<title>Pelton|Marsh &amp; Quillan – Business Card</title>
<link rel="stylesheet" href="https://fonts.googleapis.com/css2?family=Lato:wght@400;700&display=swap">
<style>
  :root {
    --backdrop: #dedede;
    --orange-deep: #b04f0c;
    --orange-mid: #d9680f;
    --orange-bright: #f98a1c;
    --orange-text: #d4650f;
    --rule: #c9560c;
    --card-white: #fbfbfb;
    --ink: #2b2b2b;
    --grey-mark: #5d5d5d;
    --white: #ffffff;
  }
  * { margin: 0; padding: 0; box-sizing: border-box; }
  html, body {
    width: 1200px;
    height: 757px;
    overflow: hidden;
    background: var(--backdrop);
    font-family: "Lato", sans-serif;
  }
  .canvas {
    position: relative;
    width: 1200px;
    height: 757px;
  }
  .card {
    position: absolute;
    top: 294px;
    width: 484px;
    height: 286px;
    border-radius: 18px;
    overflow: hidden;
  }
  .card--front {
    left: 79px;
    background: linear-gradient(90deg,
      var(--orange-deep) 0%,
      var(--orange-mid) 25%,
      var(--orange-bright) 55%,
      var(--orange-mid) 82%,
      var(--orange-deep) 100%);
  }
  .card--back {
    left: 621px;
    background: var(--card-white);
  }

  .brand {
    position: absolute;
    left: 0;
    right: 0;
    display: flex;
    align-items: center;
    justify-content: center;
    gap: 12px;
    font-weight: 400;
    white-space: nowrap;
  }
  .brand__square { display: block; flex: none; }

  .card--front .brand {
    top: 123px;
    font-size: 30px;
    color: var(--white);
  }
  .card--front .brand__square {
    width: 30px; height: 30px;
    background: var(--white);
  }

  .card--back .brand {
    top: 82px;
    font-size: 20px;
    color: var(--grey-mark);
  }
  .card--back .brand__square {
    width: 20px; height: 20px;
    background: var(--orange-text);
  }

  .holder {
    position: absolute;
    top: 166px;
    left: 0; right: 0;
    text-align: center;
  }
  .holder__name {
    font-size: 15px;
    font-weight: 700;
    color: var(--orange-text);
    letter-spacing: -0.1px;
  }
  .holder__credential {
    font-size: 10px;
    font-weight: 700;
    color: var(--ink);
    margin-left: 8px;
  }
  .holder__title {
    margin-top: 3px;
    font-size: 12.5px;
    color: var(--ink);
  }

  .rule {
    position: absolute;
    top: 229px;
    left: 0; right: 0;
    height: 2px;
    background: var(--rule);
  }

  .contact {
    position: absolute;
    top: 240px;
    left: 0; right: 0;
    text-align: center;
  }
  .contact__row {
    display: flex;
    justify-content: center;
    align-items: center;
    gap: 16px;
    font-size: 12px;
    color: var(--ink);
  }
  .contact__item {
    display: inline-flex;
    align-items: center;
    gap: 5px;
  }
  .contact__icon { width: 12px; height: 12px; fill: var(--orange-text); }
  .contact__address {
    margin-top: 5px;
    font-size: 10.5px;
    font-weight: 700;
    color: var(--orange-text);
  }
</style>
</head>
<body>
<main class="canvas">

  <section class="card card--front" aria-label="Card front">
    <div class="brand">
      <span class="brand__square"></span>
      <span class="brand__name">Pelton|Marsh &amp; Quillan</span>
    </div>
  </section>

  <section class="card card--back" aria-label="Card back">
    <div class="brand">
      <span class="brand__square"></span>
      <span class="brand__name">Pelton|Marsh &amp; Quillan</span>
    </div>

    <div class="holder">
      <p><span class="holder__name">Dr. Neil R. Whitcombe</span><span class="holder__credential">CFA</span></p>
      <p class="holder__title">Scientifique des Fusées Financières</p>
    </div>

    <div class="rule"></div>

    <div class="contact">
      <div class="contact__row">
        <span class="contact__item">
          <svg class="contact__icon" viewBox="0 0 24 24" aria-hidden="true">
            <path d="M6.6 10.8a15.1 15.1 0 0 0 6.6 6.6l2.2-2.2c.3-.3.7-.4 1-.2 1.1.4 2.3.6 3.6.6.6 0 1 .4 1 1V20c0 .6-.4 1-1 1A17 17 0 0 1 3 4c0-.6.4-1 1-1h3.5c.6 0 1 .4 1 1 0 1.3.2 2.5.6 3.6.1.3 0 .7-.2 1z"/>
          </svg>
          +1 913 555 0142
        </span>
        <span class="contact__item">
          <svg class="contact__icon" viewBox="0 0 24 24" aria-hidden="true">
            <path d="M2 5h20v14H2z M3.5 6.5 12 12.5l8.5-6" fill="var(--orange-text)"/>
            <path d="M3.5 6.8 12 12.6l8.5-5.8" fill="none" stroke="var(--white)" stroke-width="1.6"/>
          </svg>
          info@pmqadvisory.com
        </span>
      </div>
      <p class="contact__address">2275 Larkspur Avenue, Suite 310, Kansas 66214</p>
    </div>
  </section>

</main>
</body>
</html>
```